BORELTA VANE WEB

Make a website to present the different services offered by the company BORELTA VANE: - outsourcing: we look for factories in Asia to manufacture any type of product. Here we can put several examples of clients for whom we have worked putting the photos of the products that have been manufactured. - sustainability: we are the official representative for Europe and Latin America of one of the most important factories in the world of the packaging sector, it is a Chinese factory that specializes in the production of sustainable products. We can put several examples of products developed, within these products there are several categories as you can see on the website of TENWOR GROUP - http://www.tenwor-printing.example/ Today the product that we are working more and it is very fashionable is the MOLDED PULP TRAYS. - license: we have the license to manufacture and sell worldwide accessories (scarves, umbrellas, bags, wallets, etc.) of the Selvina Ortez del Campo brand. We are already selling them in several countries through our international commercial network. We could give an example of the places where it is sold (a map of googlemaps with the points, the name of the site and the address) We also have the license to manufacture and sell worldwide the "family" line of the Bright Pelunos brand. From both brands, both Selvina and Bright Pelunos we can put some presentation of the brand, photos of the products and points of sale and a place where people who want to sell these products can also contact us without having to go to the section General contact. Of both licenses we have a lot of graphic material and very nice videos that could be put in this section. We offer very different services, which must be clearly separated but we also want to see that everyone is under the umbrella of the BORELTA VANE group, a guarantee seal recognized worldwide thanks to more than 20 years of experience in the world of commerce International and very important customers who have trusted us. We can also put customers somewhere for references. Any ideas are welcome. You should see a modern, current page that conveys a feeling of being a very solid company and very committed to the environment, but not a hippy company. Very important that it is responsive and can be seen from mobile or from the computer. The cover we want to be shocking and easy to use. The slogan of BORELTA VANE is "Merit and Harmony create Sustainability"

Target Market(s)

Other companies

Coding

Coded - Design and coding required

Number of Pages Required

5+ page

Font styles to use
Sans Serif

Colors
33a6d7

Requirements
Must have
• Professional, modern image that presents all the different services.
Nice to have
• Large images, videos, corporate

```html
<!DOCTYPE html>
<html lang="en">
<head>
<meta charset="utf-8">
<title>BORELTA VANE</title>
<link href="https://fonts.googleapis.com/css2?family=Montserrat:wght@300;400;500;600;700;800&family=Open+Sans:wght@400;600&display=swap" rel="stylesheet">
<style>
:root{
  --cyan:#23d0df;
  --black:#0b0b0b;
  --dark:#1c1c1c;
  --ink:#222;
  --muted:#8a8a8a;
  --white:#fff;
  --line:#e6e6e6;
}
*{margin:0;padding:0;box-sizing:border-box}
html,body{width:1200px;height:5304px;overflow:hidden}
body{position:relative;background:var(--white);font-family:"Open Sans",Arial,sans-serif;color:var(--ink)}
.abs{position:absolute}
.heading{font-family:"Montserrat",Arial,sans-serif;font-weight:700;letter-spacing:3px;text-align:center;color:var(--ink)}
.lead{font-size:13px;line-height:22px;color:var(--muted);text-align:center}
.photo{position:absolute}

/* top bar */
.topbar{left:0;top:0;width:1200px;height:88px;background:var(--black);color:var(--white);font-family:"Montserrat",sans-serif}
.topbar .contact{top:18px;font-size:12px;display:flex;align-items:center;gap:10px}
.topbar .rule{top:44px;left:0;width:1200px;height:1px;background:#2a2a2a}
.topbar nav{top:56px;display:flex;gap:38px;font-size:12px;font-weight:600;letter-spacing:1px}
.brandbox{left:488px;top:0;width:224px;height:120px;background:var(--white);text-align:center;box-shadow:0 4px 14px rgba(0,0,0,.15)}
.brandbox .mark{width:40px;height:40px;background:var(--cyan);margin:16px auto 8px}
.brandbox .name{font-family:"Montserrat",sans-serif;font-weight:700;font-size:20px;letter-spacing:2px;color:var(--ink)}
.brandbox .tag{font-size:9px;color:var(--muted);letter-spacing:1px;margin-top:4px}

/* hero */
.hero{left:0;top:88px;width:1200px;height:592px;background:linear-gradient(90deg,#f4f6f7 0%,#e9eef0 45%,#cfd8dc 100%)}
.hero .slogan{left:120px;top:236px;font-family:"Montserrat",sans-serif;font-size:42px;font-weight:300;letter-spacing:2px;line-height:50px;color:#333}
.hl{background:var(--cyan);color:var(--white);padding:0 8px;font-weight:600}
.hero .arrow{top:542px;width:44px;height:40px;background:#444;display:flex;align-items:center;justify-content:center}

/* about */
.about-label{top:752px;left:0;width:1200px;font-size:13px;letter-spacing:3px;text-align:center;font-family:"Montserrat",sans-serif;color:#444}
.about-title{top:772px;left:0;width:1200px;text-align:center;font-family:"Montserrat",sans-serif;font-size:34px;letter-spacing:3px;color:var(--ink)}

/* outsourcing */
.outsourcing-dark{left:0;top:1000px;width:480px;height:420px;background:var(--black)}
.outsourcing-box{left:120px;top:1072px;width:480px;height:336px;background:var(--cyan);color:var(--white);padding:46px 52px}
.outsourcing-box h2{font-family:"Montserrat",sans-serif;font-size:36px;letter-spacing:3px;font-weight:700;margin-bottom:26px}
.outsourcing-box p{font-size:12px;line-height:20px;margin-bottom:14px}

/* product cards */
.product{width:224px;height:288px}
.product .shot{width:224px;height:244px}
.product .label{position:absolute;left:0;top:244px;width:200px;height:44px;background:var(--black);color:var(--white);font-family:"Montserrat",sans-serif;font-size:12px;font-weight:600;padding:8px 14px;line-height:15px}
.product .label.active{background:var(--cyan)}
.product .chev{position:absolute;left:206px;top:258px;width:14px;height:14px}
.side-arrow{width:40px;height:40px;background:#ddd;display:flex;align-items:center;justify-content:center}

/* license */
.map-card{left:740px;top:2420px;width:240px;height:104px;background:var(--white);box-shadow:0 4px 18px rgba(0,0,0,.12);border-top:4px solid var(--cyan);padding:14px 18px}
.map-card h4{font-family:"Montserrat",sans-serif;font-size:14px;margin-bottom:6px}
.map-card p{font-size:11px;line-height:16px;color:var(--muted)}

/* dark brand section */
.brands{left:0;top:2860px;width:1200px;height:940px;background:linear-gradient(180deg,#2a2a2a,#161616)}
.brand-card{width:476px;height:320px;background:var(--white)}
.brand-card .shot{position:absolute;left:12px;top:12px;width:452px;height:236px}
.brand-card .name{position:absolute;left:0;top:262px;width:380px;text-align:center;font-family:"Montserrat",sans-serif;font-weight:700;font-size:14px;letter-spacing:1px}
.brand-card .mail{position:absolute;right:24px;top:250px;width:60px;height:52px;background:var(--cyan);display:flex;align-items:center;justify-content:center}
.video-box{left:700px;top:3352px;width:388px;height:368px;background:var(--cyan);color:var(--white);padding:56px 40px}
.video-box h3{font-family:"Montserrat",sans-serif;font-size:22px;line-height:28px;letter-spacing:1px;margin-bottom:20px}
.video-box p{font-size:12px;line-height:20px;margin-bottom:12px}

/* stats */
.stats{left:0;top:3820px;width:1200px;height:108px;background:var(--black);color:var(--white)}
.stat{top:22px;display:flex;align-items:center;gap:16px}
.stat b{font-family:"Montserrat",sans-serif;font-size:34px;font-weight:700;display:block;line-height:36px}
.stat span{font-size:13px}

/* testimonials */
.testimonials{left:0;top:3928px;width:1200px;height:672px;background:linear-gradient(180deg,#262626,#141414)}
.t-card{top:4172px;width:308px;height:312px;background:#2c2c2c;text-align:center;border-bottom:5px solid var(--cyan);color:#ddd}
.t-card.light{background:var(--white);color:var(--ink)}
.t-card .avatar{width:84px;height:84px;border-radius:50%;margin:-42px auto 14px;background:linear-gradient(160deg,#c9b7a5,#6f5b4b);border:4px solid var(--white)}
.t-card h4{font-family:"Montserrat",sans-serif;font-size:16px;margin-bottom:4px}
.t-card .stars{color:var(--cyan);font-size:15px;letter-spacing:3px;margin-bottom:12px}
.t-card p{font-size:12px;line-height:19px;padding:0 28px}
.t-card .q{font-family:"Montserrat",sans-serif;font-size:48px;font-weight:800;color:var(--cyan);line-height:50px;margin-top:10px}
.dots{top:4530px;left:570px;display:flex;gap:12px}
.dots i{width:8px;height:8px;border-radius:50%;background:#666;display:block}
.dots i.on{background:var(--cyan)}

/* newsletter */
.news-input{left:364px;top:4796px;width:412px;height:50px;border:1px solid #ccc;font-size:13px;color:#888;padding:16px 18px}
.news-btn{left:776px;top:4796px;width:60px;height:50px;background:var(--cyan);display:flex;align-items:center;justify-content:center}

/* footer */
.footer{left:0;top:4920px;width:1200px;height:384px;background:var(--black);color:#bbb}
.footer h5{font-family:"Montserrat",sans-serif;color:var(--cyan);font-size:14px;letter-spacing:1px;margin-bottom:18px}
.footer ul{list-style:none;font-size:12px;line-height:24px}
.footer .copy{left:0;top:338px;width:1200px;text-align:center;font-size:11px;color:#888;border-top:1px solid #222;padding-top:14px}
.social{display:flex;gap:10px;margin-top:18px}
.social i{width:14px;height:14px;border-radius:50%;border:1px solid #bbb;display:block}
</style>
</head>
<body>

<header class="abs topbar">
  <div class="abs contact" style="left:112px">
    <svg width="14" height="14" viewBox="0 0 24 24"><path fill="#fff" d="M6.6 10.8a15 15 0 0 0 6.6 6.6l2.2-2.2a1 1 0 0 1 1-.3 11 11 0 0 0 3.6.6 1 1 0 0 1 1 1V20a1 1 0 0 1-1 1A17 17 0 0 1 3 4a1 1 0 0 1 1-1h3.5a1 1 0 0 1 1 1c0 1.3.2 2.5.6 3.6a1 1 0 0 1-.3 1z"/></svg>
    +00-555-0142-778
  </div>
  <div class="abs contact" style="right:112px">
    <svg width="16" height="12" viewBox="0 0 24 18"><rect x="1" y="1" width="22" height="16" fill="none" stroke="#fff" stroke-width="2"/><path d="M1 1l11 9 11-9" fill="none" stroke="#fff" stroke-width="2"/></svg>
    info@boreltavane.example
  </div>
  <div class="abs rule"></div>
  <nav class="abs" style="left:112px"><span>OUTSOURCING</span><span>SUSTAINABILITY</span><span>LICENSE</span></nav>
  <nav class="abs" style="right:112px"><span>ABOUT US</span><span>TESTIMONIALS</span><span>CONTACT</span></nav>
</header>

<section class="abs hero">
  <div class="photo" role="img" aria-label="Warehouse exterior with blue facade, faded background" style="left:0;top:0;width:1200px;height:592px;background:linear-gradient(90deg,rgba(255,255,255,.9) 0%,rgba(255,255,255,.6) 40%,rgba(120,150,165,.25) 100%)"></div>
  <div class="photo" role="img" aria-label="Warehouse aisle with stacked pallets and green shelving" style="left:580px;top:172px;width:508px;height:420px;background:linear-gradient(160deg,#e7e2d6 0%,#b8a88e 45%,#4f7b5c 80%,#2f4a3a 100%)"></div>
  <div class="photo" role="img" aria-label="Warehouse side view" style="left:1088px;top:172px;width:112px;height:420px;background:linear-gradient(180deg,#dfe5e8,#6f8d7a)"></div>
  <div class="abs slogan">MERIT AND<br>HARMONY <span class="hl">CREATE</span><br><span class="hl">SUSTAINABILITY</span></div>
  <div class="abs arrow" style="left:584px"><svg width="16" height="12" viewBox="0 0 16 12"><path d="M15 6H2M6 1L1 6l5 5" fill="none" stroke="#fff" stroke-width="2"/></svg></div>
  <div class="abs arrow" style="left:632px;background:#222"><svg width="16" height="12" viewBox="0 0 16 12"><path d="M1 6h13M10 1l5 5-5 5" fill="none" stroke="#fff" stroke-width="2"/></svg></div>
</section>

<div class="abs brandbox">
  <div class="mark"></div>
  <div class="name">BORELTA VANE</div>
  <div class="tag">TRADE · SOURCING · LICENSING</div>
</div>

<section>
  <div class="abs about-label">ABOUT</div>
  <div class="abs about-title">BORELTA <span class="hl" style="font-weight:700">VANE</span></div>
  <p class="abs lead" style="left:190px;top:840px;width:820px">Lorem ipsum is simply dummy text of the printing and typesetting industry. Lorem ipsum has been the industry's standard dummy text ever since the 1500s, when an unknown printer took a galley of type and scrambled it to make a type specimen book. It has survived not only five centuries, but also the leap into electronic typesetting, remaining.</p>
</section>

<section>
  <div class="abs outsourcing-dark"></div>
  <div class="photo" role="img" aria-label="Stacked shipping containers at a port under blue sky" style="left:480px;top:1000px;width:720px;height:420px;background:linear-gradient(180deg,#bcd3e3 0%,#e8eef2 30%,#a9483a 55%,#3c5f86 75%,#6c7a84 100%)"></div>
  <div class="abs outsourcing-box">
    <h2>OUTSOURCING</h2>
    <p>Lorem ipsum is simply dummy text of the printing and typesetting industry. Lorem ipsum has been the industry's standard dummy text ever since the 1500s.</p>
    <p>When an unknown printer took a galley of type and scrambled it to make a type specimen book. It has survived not only five centuries, but also the leap into electronic typesetting, remaining.</p>
  </div>
</section>

<section>
  <h2 class="abs heading" style="left:0;top:1560px;width:1200px;font-size:32px">SUSTAINABILITY</h2>
  <p class="abs lead" style="left:190px;top:1616px;width:820px">Lorem ipsum is simply dummy text of the printing and typesetting industry. Lorem ipsum has been the industry's standard dummy text ever since the 1500s, when an unknown printer took a galley of type and scrambled it to make a type specimen book. It has survived not only five centuries, but also the leap into electronic typesetting, remaining.</p>
  <div class="abs side-arrow" style="left:40px;top:1856px"><svg width="10" height="14" viewBox="0 0 10 14"><path d="M8 1L2 7l6 6" fill="none" stroke="#fff" stroke-width="2"/></svg></div>
  <div class="abs side-arrow" style="left:1120px;top:1856px"><svg width="10" height="14" viewBox="0 0 10 14"><path d="M2 1l6 6-6 6" fill="none" stroke="#fff" stroke-width="2"/></svg></div>

  <div class="abs product" style="left:112px;top:1752px">
    <div class="shot" role="img" aria-label="White wine packaging box with bottle" style="background:linear-gradient(160deg,#f2f2f2,#cfcfcf 60%,#8e8e8e)"></div>
    <div class="label">Wine Packaging<br>Boxes</div>
    <svg class="chev" viewBox="0 0 14 14"><path d="M4 1l6 6-6 6" fill="none" stroke="#555" stroke-width="2"/></svg>
  </div>
  <div class="abs product" style="left:368px;top:1752px">
    <div class="shot" role="img" aria-label="White cosmetic packaging boxes" style="background:linear-gradient(160deg,#fafafa,#e2e2e2 60%,#bdbdbd)"></div>
    <div class="label active">Cosmetic Packaging<br>Boxes</div>
    <svg class="chev" viewBox="0 0 14 14"><path d="M4 1l6 6-6 6" fill="none" stroke="#555" stroke-width="2"/></svg>
  </div>
  <div class="abs product" style="left:612px;top:1752px">
    <div class="shot" role="img" aria-label="Plain white gift packaging boxes" style="background:linear-gradient(160deg,#fff,#ececec 60%,#cfcfcf)"></div>
    <div class="label">Gift Packaging<br>Boxes</div>
    <svg class="chev" viewBox="0 0 14 14"><path d="M4 1l6 6-6 6" fill="none" stroke="#555" stroke-width="2"/></svg>
  </div>
  <div class="abs product" style="left:856px;top:1752px">
    <div class="shot" role="img" aria-label="Kraft food packaging boxes and cups" style="background:linear-gradient(160deg,#faf6ef,#e3cfaa 60%,#b58c55)"></div>
    <div class="label">Food Packaging<br>Boxes</div>
    <svg class="chev" viewBox="0 0 14 14"><path d="M4 1l6 6-6 6" fill="none" stroke="#555" stroke-width="2"/></svg>
  </div>
</section>

<section>
  <h2 class="abs heading" style="left:0;top:2180px;width:1200px;font-size:32px">LICENSE</h2>
  <p class="abs lead" style="left:190px;top:2236px;width:820px">Lorem ipsum is simply dummy text of the printing and typesetting industry. Lorem ipsum has been the industry's standard dummy text ever since the 1500s, when an unknown printer took a galley of type and scrambled it to make a type specimen book. It has survived not only five centuries, but also the leap into electronic typesetting, remaining.</p>
  <div class="photo" role="img" aria-label="World map showing points of sale with connecting routes" style="left:200px;top:2380px;width:760px;height:420px;background:radial-gradient(ellipse at 50% 50%,#e8e8e8 0%,#f3f3f3 55%,#fff 75%)"></div>
  <div class="abs map-card">
    <h4>Harlow Quay West Road</h4>
    <p>Vemmir District, Northport,<br>Harbour Province</p>
  </div>
</section>

<section class="abs brands">
  <div class="photo" role="img" aria-label="Dim warehouse interior with shelving" style="left:0;top:0;width:1200px;height:940px;background:linear-gradient(180deg,rgba(80,80,80,.5),rgba(0,0,0,.2))"></div>
</section>
<div class="abs brand-card" style="left:112px;top:2940px">
  <div class="shot" role="img" aria-label="Mother and daughter in bright outfits, brand campaign photo" style="background:linear-gradient(135deg,#e8e4de,#c99ba5 55%,#7b8aa8)"></div>
  <div class="name">SELVINA ORTEZ DEL CAMPO</div>
  <div class="mail"><svg width="22" height="16" viewBox="0 0 24 18"><rect x="1" y="1" width="22" height="16" fill="none" stroke="#fff" stroke-width="2"/><path d="M1 1l11 9 11-9" fill="none" stroke="#fff" stroke-width="2"/></svg></div>
</div>
<div class="abs brand-card" style="left:612px;top:2940px">
  <div class="shot" role="img" aria-label="Woman in a flower field, brand campaign photo" style="background:linear-gradient(160deg,#d9d2c4,#b79d7a 50%,#a7629a 80%,#6b5a3e)"></div>
  <div class="name">BRIGHT PELUNOS</div>
  <div class="mail"><svg width="22" height="16" viewBox="0 0 24 18"><rect x="1" y="1" width="22" height="16" fill="none" stroke="#fff" stroke-width="2"/><path d="M1 1l11 9 11-9" fill="none" stroke="#fff" stroke-width="2"/></svg></div>
</div>
<div class="photo" role="img" aria-label="Modern warehouse building under cloudy sky, video still" style="left:112px;top:3352px;width:588px;height:368px;background:linear-gradient(180deg,#8ea2b4 0%,#c7d1d8 40%,#5c6e7c 70%,#3b4650 100%)"></div>
<svg class="abs" style="left:350px;top:3480px" width="112" height="112" viewBox="0 0 112 112">
  <circle cx="56" cy="56" r="50" fill="rgba(0,0,0,.55)" stroke="#23d0df" stroke-width="4"/>
  <path d="M46 36l32 20-32 20z" fill="#23d0df"/>
</svg>
<div class="abs video-box">
  <h3>STANDARD DUMMY<br>TEXT EVER</h3>
  <p>Lorem ipsum is simply dummy text of the printing and typesetting industry. Lorem ipsum has been the industry's standard dummy text ever since the 1500s.</p>
  <p>When an unknown printer took a galley of type and scrambled it to make a type specimen book. It has survived not only five centuries, but also the leap into electronic typesetting.</p>
</div>

<section class="abs stats">
  <div class="abs stat" style="left:180px">
    <svg width="44" height="40" viewBox="0 0 44 40"><rect x="2" y="2" width="40" height="36" fill="none" stroke="#fff" stroke-width="2"/><circle cx="16" cy="16" r="5" fill="none" stroke="#fff" stroke-width="2"/><path d="M7 32c2-6 16-6 18 0M28 14h10M28 20h10M28 26h8" stroke="#fff" stroke-width="2" fill="none"/></svg>
    <div><b>1120+</b><span>Active Workers</span></div>
  </div>
  <div class="abs stat" style="left:500px">
    <svg width="44" height="40" viewBox="0 0 44 40"><path d="M2 30h30l8-12H34V8H14v10H2z" fill="none" stroke="#fff" stroke-width="2"/><circle cx="10" cy="34" r="3" fill="#fff"/><circle cx="28" cy="34" r="3" fill="#fff"/></svg>
    <div><b>520+</b><span>Total Products</span></div>
  </div>
  <div class="abs stat" style="left:820px">
    <svg width="40" height="40" viewBox="0 0 40 40"><circle cx="20" cy="20" r="17" fill="none" stroke="#fff" stroke-width="2"/><path d="M3 20h34M20 3c-8 9-8 25 0 34M20 3c8 9 8 25 0 34" fill="none" stroke="#fff" stroke-width="2"/></svg>
    <div><b>130+</b><span>Countries</span></div>
  </div>
</section>

<section class="abs testimonials">
  <div class="photo" role="img" aria-label="Dark industrial interior backdrop" style="left:0;top:0;width:1200px;height:672px;background:linear-gradient(180deg,rgba(60,60,60,.4),rgba(0,0,0,.4))"></div>
  <h2 class="abs heading" style="left:0;top:80px;width:1200px;font-size:32px;color:#fff">TESTIMONIALS</h2>
  <p class="abs lead" style="left:190px;top:132px;width:820px;color:#bbb">Lorem ipsum is simply dummy text of the printing and typesetting industry. Lorem ipsum has been the industry's standard dummy text ever since the 1500s, when an unknown printer took a galley of type and scrambled it.</p>
</section>
<div class="abs t-card light" style="left:112px">
  <div class="avatar" role="img" aria-label="Client portrait"></div>
  <h4>Dorian Halvek</h4><div class="stars">★★★★★</div>
  <p>Lorem ipsum is simply dummy text of the printing and typesetting industry. Lorem ipsum has been the industry.</p>
  <div class="q">“</div>
</div>
<div class="abs t-card" style="left:446px">
  <div class="avatar" role="img" aria-label="Client portrait"></div>
  <h4>Mirela Joss</h4><div class="stars">★★★★★</div>
  <p>Lorem ipsum is simply dummy text of the printing and typesetting industry. Lorem ipsum has been the industry.</p>
  <div class="q">“</div>
</div>
<div class="abs t-card" style="left:780px">
  <div class="avatar" role="img" aria-label="Client portrait"></div>
  <h4>Tobin Arqué</h4><div class="stars">★★★★★</div>
  <p>Lorem ipsum is simply dummy text of the printing and typesetting industry. Lorem ipsum has been the industry.</p>
  <div class="q">“</div>
</div>
<div class="abs dots"><i class="on"></i><i></i><i></i></div>

<section>
  <h2 class="abs heading" style="left:0;top:4680px;width:1200px;font-size:34px">NEWLETTER</h2>
  <p class="abs lead" style="left:0;top:4740px;width:1200px;color:#555">Get product updates and live offers right to your inbox</p>
  <div class="abs news-input">Enter your email</div>
  <div class="abs news-btn"><svg width="20" height="18" viewBox="0 0 20 18"><path d="M1 1l18 8-18 8 3-8z" fill="#fff"/></svg></div>
</section>

<footer class="abs footer">
  <div class="abs" style="left:112px;top:60px;width:260px">
    <div style="display:flex;align-items:center;gap:10px"><div style="width:26px;height:26px;background:var(--cyan)"></div><span style="font-family:Montserrat,sans-serif;font-weight:700;font-size:18px;color:#fff;letter-spacing:2px">BORELTA VANE</span></div>
    <p style="font-size:12px;line-height:20px;margin-top:16px">Lorem ipsum is simply dummy text of the printing and typesetting industry.</p>
    <div class="social"><i></i><i></i><i></i><i></i><i></i></div>
  </div>
  <div class="abs" style="left:408px;top:56px"><h5>QUICK LINKS</h5><ul><li>Outsourcing</li><li>Sustainability</li><li>License</li><li>About us</li><li>Testimonials</li><li>Contact us</li></ul></div>
  <div class="abs" style="left:612px;top:56px"><h5>CONTACTS</h5><ul><li>4410 Corran Ave, Lindmoor,</li><li>NV, 00421</li><li>+00-555-0142-778</li><li>info@boreltavane.example</li></ul></div>
  <div class="abs" style="left:864px;top:56px"><h5>COUNTRIES</h5><ul><li>USA</li><li>China</li><li>United Kingdom</li><li>Argentina</li><li>Mexico</li></ul></div>
  <div class="abs copy">Copyright © Borelta Vane. All Rights Reserved</div>
</footer>

</body>
</html>
```